Young, dynamic furniture company requires leaflet design

We require a new leaflet for our modern furniture company which supplies furniture and appliances to the property and development market.
Bramblecourt Furniture has become one of the leading furniture & appliance suppliers to the property market withing London. With over 10 years experience, we have increased our business to supply not only Private Landlords and Managing Agents, but also Property Developers, Housing Associations and Local Councils.
We offer not only a complete range of furniture which includes beds, wardrobes, dining sets and sofas, but also a high quality, full delivery and assembly service to help you with all our furnishing needs.

Target Market(s)

Private Landlords, Developers, Letting & Managing Agents

Industry/Entity Type

Furniture Store

Font styles to use
Sans Serif

Colors
0255a3
3176b5
85abd2
cfdeed
eaf1f7

Requirements
Must have
• Contact details,
• Our services:
• FREE next day delivery within the M25
• Free furniture assembly
• Free key pick up & drop off
• Free furniture removal (on a like-for-like basis)
• All types of furniture supplied - from basic to luxury

```html
<!DOCTYPE html>
<html lang="en">
<head>
<meta charset="utf-8">
<title>Bramblecourt Furniture – Leaflet</title>
<link rel="stylesheet" href="https://fonts.googleapis.com/css2?family=Lato:ital,wght@0,400;0,700;1,400;1,700&family=Oswald:wght@300&family=Archivo:wght@600&display=swap">
<style>
  :root {
    --navy: #1d3a7a;
    --bright-blue: #1a86e8;
    --mid-blue: #3176b5;
    --charcoal: #2a2a2a;
    --text-dark: #2b2b2b;
    --grey-band: #d4d4d4;
    --white: #ffffff;
    --photo-light: #eef1f4;
    --photo-dark: #9aa0a7;
  }
  html, body {
    margin: 0;
    padding: 0;
    width: 871px;
    height: 1200px;
    overflow: hidden;
    background: var(--white);
  }
  .leaflet {
    position: relative;
    width: 871px;
    height: 1200px;
    overflow: hidden;
    background: var(--white);
    font-family: "Lato", sans-serif;
  }
  .leaflet__shapes {
    position: absolute;
    inset: 0;
  }
  .brand {
    position: absolute;
    left: 34px;
    top: 122px;
    display: flex;
    align-items: center;
    gap: 12px;
  }
  .brand__square {
    width: 22px;
    height: 22px;
    background: var(--mid-blue);
  }
  .brand__name {
    font-family: "Lato", sans-serif;
    font-weight: 700;
    font-size: 24px;
    color: var(--navy);
    letter-spacing: 0.3px;
  }
  .brand__tagline {
    position: absolute;
    left: 68px;
    top: 156px;
    font-family: "Lato", sans-serif;
    font-size: 12px;
    letter-spacing: 1.5px;
    color: var(--text-dark);
  }
  .services-heading {
    position: absolute;
    left: 74px;
    top: 582px;
    margin: 0;
    font-style: italic;
    font-weight: 700;
    font-size: 44px;
    line-height: 56px;
    color: var(--white);
    text-align: center;
    width: 240px;
  }
  .promise {
    position: absolute;
    right: 30px;
    top: 566px;
    margin: 0;
    text-align: right;
  }
  .promise__line1 {
    display: block;
    font-family: "Oswald", sans-serif;
    font-weight: 300;
    font-size: 96px;
    line-height: 104px;
    color: var(--bright-blue);
    letter-spacing: -1px;
  }
  .promise__line2 {
    display: block;
    font-family: "Archivo", sans-serif;
    font-weight: 600;
    font-size: 58px;
    line-height: 60px;
    color: var(--navy);
  }
  .service-list {
    position: absolute;
    left: 140px;
    top: 768px;
    margin: 0;
    padding: 0;
    list-style: none;
  }
  .service-list__item {
    display: flex;
    align-items: center;
    height: 72px;
  }
  .service-list__badge {
    width: 52px;
    height: 52px;
    border-radius: 50%;
    background: var(--navy);
    border: 3px solid var(--white);
    box-shadow: 0 0 0 1px var(--navy);
    color: var(--white);
    font-style: italic;
    font-weight: 700;
    font-size: 22px;
    display: flex;
    align-items: center;
    justify-content: center;
    margin-right: 20px;
  }
  .service-list__text {
    font-style: italic;
    font-weight: 700;
    font-size: 27px;
    color: var(--text-dark);
  }
  .range-band {
    position: absolute;
    left: 165px;
    right: 0;
    top: 1075px;
    height: 47px;
    background: var(--grey-band);
    color: var(--navy);
    font-size: 26px;
    line-height: 47px;
    text-align: center;
    letter-spacing: 0.3px;
  }
  .contact {
    position: absolute;
    left: 165px;
    right: 0;
    top: 1122px;
    height: 78px;
  }
  .contact__details {
    position: absolute;
    left: 36px;
    top: 10px;
    color: var(--white);
    font-style: italic;
    font-weight: 700;
    font-size: 13px;
    line-height: 27px;
  }
  .contact__row {
    display: flex;
    align-items: center;
    gap: 8px;
  }
  .contact__row--phone {
    font-size: 17px;
    font-weight: 400;
  }
  .contact__call {
    position: absolute;
    right: 44px;
    top: 10px;
    color: var(--white);
    font-style: italic;
    font-weight: 700;
    font-size: 22px;
    line-height: 28px;
    text-align: center;
  }
  .contact__call-number {
    font-weight: 700;
    font-size: 20px;
  }
</style>
</head>
<body>
<div class="leaflet">
  <svg class="leaflet__shapes" width="871" height="1200" viewBox="0 0 871 1200" xmlns="http://www.w3.org/2000/svg">
    <defs>
      <linearGradient id="roomTones" x1="0" y1="0" x2="1" y2="1">
        <stop offset="0" stop-color="var(--photo-dark)"/>
        <stop offset="0.45" stop-color="var(--photo-light)"/>
        <stop offset="1" stop-color="#c8ccd1"/>
      </linearGradient>
    </defs>
    <polygon role="img" aria-label="Photograph of a furnished bedroom with white bedding, black throw and dark furniture by a bright window"
             points="0,275 187,298 570,0 871,0 871,274 258,749 0,700" fill="url(#roomTones)"/>
    <polyline points="0,272 187,295 566,0" fill="none" stroke="var(--navy)" stroke-width="5"/>
    <polygon class="band band--bright" points="871,274 871,322 306,749 258,749" fill="var(--bright-blue)"/>
    <polygon class="band band--navy" points="871,322 871,356 342,752 306,749" fill="var(--navy)"/>
    <rect class="sidebar" x="0" y="697" width="165" height="503" fill="var(--charcoal)"/>
    <polygon class="services-flag" points="0,641 220,543 354,669 258,749 0,676" fill="var(--bright-blue)"/>
    <polygon class="services-flag__base" points="0,684 258,752 300,749 258,766 0,700" fill="var(--bright-blue)"/>
    <polygon class="contact-bg" points="165,1122 690,1122 672,1200 165,1200" fill="var(--bright-blue)"/>
    <polygon class="contact-call-bg" points="690,1122 871,1122 871,1200 672,1200" fill="var(--navy)"/>
  </svg>

  <div class="brand">
    <span class="brand__square"></span>
    <span class="brand__name">Bramblecourt Furniture</span>
  </div>
  <div class="brand__tagline">TRADE FURNITURE SOLUTIONS</div>

  <h2 class="services-heading">OUR<br>SERVICES:</h2>

  <h1 class="promise">
    <span class="promise__line1">THE BCF</span>
    <span class="promise__line2">PROMISE</span>
  </h1>

  <ul class="service-list">
    <li class="service-list__item"><span class="service-list__badge">01</span><span class="service-list__text">FREE next day delivery within the M25</span></li>
    <li class="service-list__item"><span class="service-list__badge">02</span><span class="service-list__text">Free furniture assembly</span></li>
    <li class="service-list__item"><span class="service-list__badge">03</span><span class="service-list__text">Free key pick up &amp; drop off</span></li>
    <li class="service-list__item"><span class="service-list__badge">04</span><span class="service-list__text">Free furniture removal (on a like-for-like basis)</span></li>
  </ul>

  <div class="range-band">All types of furniture supplied - from basic to luxury</div>

  <div class="contact">
    <div class="contact__details">
      <div class="contact__row">
        <svg width="16" height="15" viewBox="0 0 16 15" aria-hidden="true"><path d="M8 1 L15 7 H13 V14 H9.5 V10 H6.5 V14 H3 V7 H1 Z" fill="var(--white)"/></svg>
        <span>Unit 7B Harrowgate Trade Park, Northfield, London N19 4QP</span>
      </div>
      <div class="contact__row contact__row--phone">
        <svg width="16" height="15" viewBox="0 0 16 15" aria-hidden="true"><rect x="4" y="1" width="8" height="4" fill="var(--white)"/><rect x="1" y="5" width="14" height="6" rx="1" fill="var(--white)"/><rect x="4" y="9" width="8" height="5" fill="var(--white)" stroke="var(--bright-blue)" stroke-width="1"/></svg>
        <span>020 7946 0321</span>
      </div>
    </div>
    <div class="contact__call">CALL US:<br><span class="contact__call-number">020 7946 0388</span></div>
  </div>
</div>
</body>
</html>
```